Dental office needs a sticker designed for promotions

My dental practice needs a sticker designed to be used on patient bags, promotional items, and give aways like retainer cases. The stickers will be round, 3 inches in diameter. I may have some smaller round stickers printed as will, but will use the same design. The logo should be the primary focus and must use brand colors of red and white. I would like to include our information such as the website (www.kpvsmile-example.com), phone number (555)314-9086, and social media info - Facebook @brightoakdental, Instagram @smiles_at_willow_creek_co.

```html
<!DOCTYPE html>
<html lang="en">
<head>
<meta charset="utf-8">
<title>Kingsport Valley Smiles – Promotional Sticker</title>
<link href="https://fonts.googleapis.com/css2?family=Roboto:wght@300;700&family=Roboto+Condensed:wght@700&display=swap" rel="stylesheet">
<style>
  :root {
    --backdrop: #bbbcbf;
    --sticker-white: #ffffff;
    --brand-red: #d81e43;
    --brand-red-deep: #8f1a2b;
    --logo-red: #cf2450;
  }
  * { margin: 0; padding: 0; box-sizing: border-box; }
  html, body {
    width: 1200px;
    height: 1200px;
    overflow: hidden;
    background: var(--backdrop);
  }
  .canvas {
    position: relative;
    width: 1200px;
    height: 1200px;
  }
  .sticker-art {
    position: absolute;
    inset: 0;
    width: 1200px;
    height: 1200px;
  }
  .website {
    font-family: "Roboto", sans-serif;
    font-weight: 700;
    font-size: 28px;
    fill: var(--sticker-white);
  }
  .brand-name {
    font-family: "Roboto", sans-serif;
    font-weight: 700;
    fill: var(--logo-red);
  }
  .phone {
    font-family: "Roboto", sans-serif;
    font-weight: 300;
    font-size: 84px;
    fill: var(--sticker-white);
  }
  .social-handle {
    font-family: "Roboto Condensed", sans-serif;
    font-weight: 700;
    font-size: 31px;
    fill: var(--brand-red-deep);
  }
  .social-marker { fill: var(--brand-red-deep); }
</style>
</head>
<body>
<main class="canvas">
  <svg class="sticker-art" viewBox="0 0 1200 1200" xmlns="http://www.w3.org/2000/svg">
    <defs>
      <clipPath id="inner-circle">
        <circle cx="600" cy="600" r="412"/>
      </clipPath>
      <filter id="sticker-shadow" x="-10%" y="-10%" width="120%" height="120%">
        <feDropShadow dx="0" dy="8" stdDeviation="10" flood-color="#000" flood-opacity="0.18"/>
      </filter>
    </defs>

    <circle class="sticker-base" cx="600" cy="600" r="450" fill="var(--sticker-white)" filter="url(#sticker-shadow)"/>

    <g class="top-ribbon">
      <path d="M336,282 C430,220 570,186 670,192 C745,197 800,228 838,262 C770,300 690,324 610,318 C520,310 420,272 336,282 Z" fill="var(--brand-red-deep)"/>
      <path d="M336,282 C430,220 570,186 670,192 C745,197 800,228 830,258 C760,286 690,306 610,300 C520,294 420,270 336,282 Z" fill="var(--brand-red)"/>
      <text class="website" x="600" y="262" text-anchor="middle">www.kpvsmile-example.com</text>
    </g>

    <g class="brand-lockup">
      <text class="brand-name" x="600" y="455" text-anchor="middle" font-size="72">Kingsport Valley</text>
      <text class="brand-name" x="600" y="545" text-anchor="middle" font-size="64" letter-spacing="6">SMILES</text>
    </g>

    <g class="bottom-wave" clip-path="url(#inner-circle)">
      <path d="M212,740 C330,676 450,655 560,672 C690,692 820,728 910,686 C960,660 990,600 1012,520 L1100,520 L1100,1100 L100,1100 Z" fill="var(--brand-red-deep)"/>
      <path d="M212,740 C330,676 450,655 560,672 C680,692 800,738 900,724 C960,712 995,670 1014,610 L1100,600 L1100,1100 L100,1100 Z" fill="var(--brand-red)"/>
    </g>

    <text class="phone" x="600" y="812" text-anchor="middle">(555)314-9086</text>

    <g class="social-list">
      <rect class="social-marker" x="420" y="861" width="31" height="31" rx="4"/>
      <text class="social-handle" x="463" y="889">smiles_at_willow_creek_co</text>
      <rect class="social-marker" x="420" y="918" width="31" height="31" rx="4"/>
      <text class="social-handle" x="463" y="946">brightoakdental</text>
    </g>
  </svg>
</main>
</body>
</html>
```